A modern web page for a software product

We need a web page for a software product, which is an advanced solution based on Machine Learning and Natural Language processing. We already have a logo of the product and expect the web page to be inline with the logo colors. The design should be for one page web site with scrolled sections - details of the content and guidelines in the attachments.

Target Market(s)

software company

Industry/Entity Type

It Company

Number of Pages Required

1 page

Colors

Designer to choose colors to be used in the design.

Requirements
Must have
• - modern icons and graphics
• - inline with the logo colors
• - be related to Machine Learining, AI, data processing
• - should have two language versions: english and polish both are attached.
Nice to have
• - animation/motion
Should not have
• - any photos embedded

```html
<!DOCTYPE html>
<html lang="en">
<head>
<meta charset="utf-8">
<title>Klarvion – Personal Data Discovery</title>
<link href="https://fonts.googleapis.com/css2?family=Roboto+Condensed:wght@400;700&family=Open+Sans:wght@400;600&display=swap" rel="stylesheet">
<style>
  :root{
    --navy:#1b2a52;
    --navy-line:#33477a;
    --teal:#2fb1b9;
    --teal-dark:#1f8f98;
    --teal-light:#55c6cc;
    --hero-top:#5fb4e6;
    --hero-mid:#2480c6;
    --hero-bottom:#0e4c8c;
    --dark:#2e3236;
    --dark-text:#e8eef2;
    --muted:#9aa7b0;
    --white:#ffffff;
    --footer:#5b6570;
    --page:#ffffff;
  }
  *{box-sizing:border-box;margin:0;padding:0}
  html,body{width:882px;height:1200px;overflow:hidden;background:var(--page)}
  body{font-family:"Open Sans",sans-serif;color:var(--navy);position:relative}
  .page{position:relative;width:882px;height:1200px}

  .hero{position:absolute;left:0;top:0;width:882px;height:338px;
    background:radial-gradient(circle at 15% 10%,var(--hero-top) 0%,transparent 40%),
               radial-gradient(circle at 85% 30%,#3d9ad8 0%,transparent 45%),
               linear-gradient(180deg,var(--hero-mid) 0%,var(--hero-bottom) 100%);}
  .logo{position:absolute;left:12px;top:10px;display:flex;align-items:center;gap:6px;
    font-family:"Roboto Condensed",sans-serif;font-weight:700;font-size:17px;color:var(--white);}
  .logo-mark{width:12px;height:12px;background:var(--teal);}
  .nav{position:absolute;left:96px;top:0;width:786px;height:40px;display:flex;}
  .nav-item{flex:1;background:var(--navy);border-left:1px solid var(--navy-line);
    color:var(--white);font-family:"Roboto Condensed",sans-serif;font-size:8.5px;
    text-transform:uppercase;text-align:center;display:flex;align-items:center;justify-content:center;
    line-height:1.25;padding:0 6px;letter-spacing:.2px;white-space:nowrap}
  .nav-item.active{background:#22356a}

  .tile{position:absolute;background:linear-gradient(180deg,var(--teal-light),var(--teal));
    border:1px solid rgba(255,255,255,.35);display:flex;align-items:center;gap:10px;padding:8px 12px;
    box-shadow:0 2px 6px rgba(0,20,60,.25)}
  .tile-icon{flex:0 0 24px;height:24px;border:1.5px solid var(--white);display:flex;align-items:center;justify-content:center}
  .tile-title{font-family:"Roboto Condensed",sans-serif;font-weight:700;font-size:9.5px;color:var(--white);text-transform:uppercase;line-height:1.3}
  .tile-list{margin-top:4px;list-style:none;font-size:6.5px;color:var(--white);line-height:1.45}
  .tile-list li::before{content:"› "}

  .features{position:absolute;left:0;top:338px;width:882px;height:522px;background:var(--dark)}
  .feature{position:absolute;width:210px;text-align:center;color:var(--dark-text)}
  .feature-icon{width:62px;height:62px;margin:0 auto 10px;border:2px solid var(--dark-text);border-radius:50%;
    display:flex;align-items:center;justify-content:center}
  .feature-title{font-family:"Roboto Condensed",sans-serif;font-weight:700;font-size:10px;text-transform:uppercase;line-height:1.3}
  .feature-note{font-size:7px;color:var(--muted);margin-top:3px;line-height:1.4}

  .cap{position:absolute;width:410px}
  .cap-head{height:22px;background:var(--navy);color:var(--white);display:flex;align-items:center;
    font-family:"Roboto Condensed",sans-serif;font-weight:700;font-size:8.5px;text-transform:uppercase}
  .cap-num{width:22px;height:22px;background:var(--teal);margin-right:10px;display:flex;align-items:center;justify-content:center}
  .cap-list{list-style:none;border:1px solid #cfd8e2;border-top:none;padding:5px 10px 6px 32px;font-size:7px;line-height:1.6;text-transform:uppercase;color:var(--navy)}
  .cap-list li::before{content:"• ";color:var(--teal)}

  .footer{position:absolute;left:0;top:1130px;width:882px;height:28px;background:var(--footer);display:flex}
  .footer-cell{flex:1;color:var(--white);font-size:8px;display:flex;align-items:center;justify-content:center;border-right:1px solid #6d7883}
  .copyright{position:absolute;left:0;top:1172px;width:882px;text-align:center;font-size:7px;color:#7a848d}
</style>
</head>
<body>
<div class="page">

  <section class="hero" role="img" aria-label="Soft blue glowing background with blurred light spots">
    <div class="logo"><span class="logo-mark"></span>Klarvion</div>
    <nav class="nav">
      <div class="nav-item active">Discovery and classification<br>of personal data</div>
      <div class="nav-item">Councils management<br>support</div>
      <div class="nav-item">Unified registry<br>of all personal data</div>
      <div class="nav-item">Support:<br>data flows and instructions / sources</div>
    </nav>

    <div class="tile" style="left:100px;top:62px;width:340px;height:84px">
      <div class="tile-icon"><svg width="14" height="14" viewBox="0 0 14 14"><circle cx="6" cy="6" r="4" fill="none" stroke="#fff" stroke-width="1.5"/><path d="M9 9l4 4" stroke="#fff" stroke-width="1.5"/></svg></div>
      <div>
        <div class="tile-title">Detection of personal and sensitive data for GDPR compliance</div>
        <ul class="tile-list">
          <li>in structured sources (databases, tables, registries)</li>
          <li>in unstructured sources (documents, emails, scans, notes)</li>
          <li>in mixed sources with combined text and record fields</li>
          <li>with reports on the location and volume of found data</li>
        </ul>
      </div>
    </div>
    <div class="tile" style="left:470px;top:92px;width:310px;height:36px">
      <div class="tile-icon"><svg width="14" height="14" viewBox="0 0 14 14"><rect x="2" y="2" width="4" height="4" fill="#fff"/><rect x="8" y="2" width="4" height="4" fill="#fff"/><rect x="2" y="8" width="4" height="4" fill="#fff"/><rect x="8" y="8" width="4" height="4" fill="#fff"/></svg></div>
      <div class="tile-title">Fast categorizing and classification of data sources</div>
    </div>

    <div class="tile" style="left:100px;top:160px;width:340px;height:36px">
      <div class="tile-icon"><svg width="14" height="14" viewBox="0 0 14 14"><ellipse cx="7" cy="3.5" rx="5" ry="2" fill="none" stroke="#fff" stroke-width="1.3"/><path d="M2 3.5v7c0 1.1 2.2 2 5 2s5-.9 5-2v-7" fill="none" stroke="#fff" stroke-width="1.3"/></svg></div>
      <div class="tile-title">Unified data registry for easier compliance guidance</div>
    </div>
    <div class="tile" style="left:470px;top:160px;width:310px;height:36px">
      <div class="tile-icon"><svg width="14" height="14" viewBox="0 0 14 14"><rect x="3" y="6" width="8" height="6" fill="none" stroke="#fff" stroke-width="1.3"/><path d="M5 6V4a2 2 0 0 1 4 0v2" fill="none" stroke="#fff" stroke-width="1.3"/></svg></div>
      <div class="tile-title">Management of consents and data access policies</div>
    </div>

    <div class="tile" style="left:100px;top:210px;width:340px;height:36px">
      <div class="tile-icon"><svg width="14" height="14" viewBox="0 0 14 14"><path d="M2 12V8M6 12V4M10 12V6" stroke="#fff" stroke-width="2"/></svg></div>
      <div class="tile-title">Customizable analytics and reporting</div>
    </div>
    <div class="tile" style="left:470px;top:206px;width:310px;height:44px">
      <div class="tile-icon"><svg width="14" height="14" viewBox="0 0 14 14"><path d="M2 7h10M8 3l4 4-4 4" fill="none" stroke="#fff" stroke-width="1.5"/></svg></div>
      <div class="tile-title">Ability to integrate with tools for data anonymization or pseudonymization</div>
    </div>

    <div class="tile" style="left:265px;top:268px;width:350px;height:36px">
      <div class="tile-icon"><svg width="14" height="14" viewBox="0 0 14 14"><path d="M5 3L1 7l4 4M9 3l4 4-4 4" fill="none" stroke="#fff" stroke-width="1.5"/></svg></div>
      <div class="tile-title">RESTful API for system management and integration</div>
    </div>
  </section>

  <section class="features">
    <div class="feature" style="left:56px;top:38px">
      <div class="feature-icon"><svg width="30" height="30" viewBox="0 0 30 30"><rect x="7" y="4" width="16" height="22" fill="none" stroke="#e8eef2" stroke-width="2"/><path d="M11 11h8M11 16h8M11 21h5" stroke="#e8eef2" stroke-width="2"/></svg></div>
      <div class="feature-title">Internal audits and verifications of the current status</div>
      <div class="feature-note">in preparation for incoming GDPR compliance</div>
    </div>
    <div class="feature" style="left:336px;top:38px">
      <div class="feature-icon"><svg width="30" height="30" viewBox="0 0 30 30"><rect x="5" y="7" width="20" height="16" fill="none" stroke="#e8eef2" stroke-width="2"/><text x="15" y="19" fill="#e8eef2" font-size="9" font-family="Open Sans,sans-serif" text-anchor="middle">A</text></svg></div>
      <div class="feature-title">Cataloging sources that<br>store sensitive data</div>
    </div>
    <div class="feature" style="left:616px;top:38px">
      <div class="feature-icon"><svg width="30" height="30" viewBox="0 0 30 30"><ellipse cx="15" cy="8" rx="9" ry="3.5" fill="none" stroke="#e8eef2" stroke-width="2"/><path d="M6 8v14c0 2 4 3.5 9 3.5s9-1.5 9-3.5V8M6 15c0 2 4 3.5 9 3.5s9-1.5 9-3.5" fill="none" stroke="#e8eef2" stroke-width="2"/></svg></div>
      <div class="feature-title">Defining the registry of personal data to implement rights to information, forgetfulness, data transfer</div>
    </div>

    <div class="feature" style="left:56px;top:250px">
      <div class="feature-icon"><svg width="30" height="30" viewBox="0 0 30 30"><path d="M24 15a9 9 0 1 1-3-6.7" fill="none" stroke="#e8eef2" stroke-width="2"/><path d="M22 4v5h-5" fill="none" stroke="#e8eef2" stroke-width="2"/></svg></div>
      <div class="feature-title">Continuous monitoring and<br>classification of data</div>
    </div>
    <div class="feature" style="left:336px;top:250px">
      <div class="feature-icon"><svg width="30" height="30" viewBox="0 0 30 30"><path d="M5 24h20M8 24V16M13 24V11M18 24V14M23 24V7" stroke="#e8eef2" stroke-width="2.5"/></svg></div>
      <div class="feature-title">Use collected data to<br>create additional business value</div>
    </div>
    <div class="feature" style="left:616px;top:250px">
      <div class="feature-icon"><svg width="30" height="30" viewBox="0 0 30 30"><path d="M4 9h8l2 3h12v12H4z" fill="none" stroke="#e8eef2" stroke-width="2"/></svg></div>
      <div class="feature-title">Classification of documents</div>
      <div class="feature-note">contracts, invoices, CVs and forms sorted<br>by content to speed up reviews<br>and assign retention rules</div>
    </div>
  </section>

  <section class="cap" style="left:23px;top:876px">
    <div class="cap-head"><span class="cap-num">1</span>Ready for implementation for detection of personal data</div>
    <ul class="cap-list">
      <li>Identity card data</li>
      <li>Names of data processors</li>
      <li>Personal and contact details</li>
      <li>Bank accounts and payment data</li>
    </ul>
  </section>
  <section class="cap" style="left:449px;top:876px">
    <div class="cap-head"><span class="cap-num">2</span>Find personal data detection leads "right" kind of companies</div>
    <ul class="cap-list">
      <li>Medical and insurance providers</li>
      <li>Banks and financial services</li>
      <li>Public sector offices</li>
      <li>Custom models for data detection specific to your organization needs</li>
    </ul>
  </section>
  <section class="cap" style="left:23px;top:990px">
    <div class="cap-head"><span class="cap-num">3</span>Supports structured and unstructured data sources</div>
    <ul class="cap-list">
      <li>Files: internal and shared, content management, archives</li>
      <li>Mail servers and mailboxes, contacts and calendars</li>
      <li>Relational databases</li>
      <li>File and cloud storages</li>
      <li>Data exchange buses</li>
    </ul>
  </section>
  <section class="cap" style="left:449px;top:990px">
    <div class="cap-head"><span class="cap-num">4</span>Ready for high performance processing</div>
    <ul class="cap-list">
      <li>Distributed processing on many nodes</li>
      <li>Scalable cluster deployment</li>
      <li>Fast indexing of large archives</li>
    </ul>
  </section>

  <footer class="footer">
    <div class="footer-cell">Klarvion Sp. z o.o.</div>
    <div class="footer-cell">www.klarvion.example</div>
    <div class="footer-cell">+48 000 000 000</div>
    <div class="footer-cell">hello@klarvion.example</div>
  </footer>
  <div class="copyright">© Copyright 2018</div>
</div>
</body>
</html>
```